New Wix Website Design Project For New Finance Company

Create new design for a new page. Website should match existing theme of presentation deck, business card and logo attached to the brief. The site will have five pages

1) Home
2) Investment Criteria
3) Approach
4) Team
5) Contact

Some examples include
http://www.kestelvalefunds.com/

Although not a requirement, if the below white fence or similar could be added subtly to the sight as well, that would be great.

https://www.brovix.com/search?q=white+fence+horse&src=img&page=1#view=tr8KpL2wQz:

Target Market(s)

Business Professionals

Font styles to use
Sans Serif

Colors

Designer to choose colors to be used in the design.

Requirements
Must have
• Clean layout. Easy to upload header and footer.

```html
<!DOCTYPE html>
<html lang="en">
<head>
<meta charset="utf-8">
<title>Harrow Creek Capital</title>
<link rel="stylesheet" href="https://fonts.googleapis.com/css2?family=Raleway:ital,wght@0,400;0,500;0,600;0,700;0,800;1,600&display=swap">
<style>
:root{
  --blue:#0a6ebd;
  --blue-deep:#0860a8;
  --ink:#2b2b2b;
  --muted:#7a7a7a;
  --line:#c9c9c9;
  --grid:#ececec;
  --white:#ffffff;
  --black:#050505;
  --field:#d8d8d8;
}
*{margin:0;padding:0;box-sizing:border-box}
html,body{width:1200px;height:3000px;overflow:hidden;background:var(--white)}
body{font-family:"Raleway",Arial,sans-serif;color:var(--ink);position:relative}

/* header */
.site-header{position:absolute;left:0;top:0;width:1200px;height:104px;background:var(--white)}
.brand{position:absolute;left:76px;top:33px;white-space:nowrap;font-weight:700;font-size:28px;line-height:38px;color:var(--blue)}
.main-nav{position:absolute;top:32px;right:76px;display:flex;align-items:center}
.main-nav a{display:block;font-size:15px;font-weight:500;color:var(--ink);text-decoration:none;padding:0 15px;height:42px;line-height:42px;white-space:nowrap}
.main-nav a.active{background:var(--blue);color:var(--white);padding:0 20px;margin-right:14px}

/* hero */
.hero{position:absolute;left:0;top:104px;width:1200px;height:572px;overflow:hidden}
.hero-photo{position:absolute;inset:0;background:linear-gradient(180deg,#24331f 0%,#3a4a2c 38%,#5b4a36 52%,#4a5a30 64%,#3d5226 100%)}
.hero-shade{position:absolute;inset:0;background:rgba(0,0,0,.22)}
.hero-title{position:absolute;top:214px;width:100%;text-align:center;color:var(--white);font-weight:700;font-size:62px;letter-spacing:2px;white-space:nowrap}
.hero-tag{position:absolute;top:292px;width:100%;text-align:center;color:var(--white);font-style:italic;font-weight:600;font-size:18px}
.btn{position:absolute;display:block;text-align:center;font-size:20px;font-weight:500;color:var(--white);text-decoration:none;letter-spacing:.5px;white-space:nowrap}
.btn-solid{background:var(--blue)}
.btn-outline{border:1.5px solid var(--white)}
.hero .btn{left:502px;top:340px;width:196px;height:52px;line-height:52px}
.hero-arrow{position:absolute;top:262px}

/* welcome */
.welcome{position:absolute;left:0;top:676px;width:1200px;height:418px;background:var(--blue);color:var(--white);text-align:center}
.section-title{font-size:42px;font-weight:700;letter-spacing:.5px;white-space:nowrap}
.welcome .section-title{position:absolute;top:56px;width:100%}
.welcome-copy{position:absolute;left:210px;top:128px;width:780px;font-size:13.5px;line-height:25px}
.welcome-copy p+p{margin-top:14px}
.welcome .btn{left:508px;top:300px;width:184px;height:52px;line-height:50px}

/* criteria */
.criteria{position:absolute;left:0;top:1094px;width:1200px;height:738px}
.criteria .section-title{position:absolute;top:56px;width:100%;text-align:center}
.accent{color:var(--blue)}
.chart{position:absolute;left:170px;top:150px}
.criteria-copy{position:absolute;left:218px;top:570px;width:500px;font-size:13.5px;line-height:27px;color:var(--muted)}
.criteria .btn{left:822px;top:588px;width:180px;height:50px;line-height:50px}

/* approach */
.approach{position:absolute;left:0;top:1832px;width:1200px;height:490px;background:var(--blue)}
.approach .section-title{position:absolute;top:54px;width:100%;text-align:center;color:var(--white)}
.approach .dark{color:var(--ink)}
.pillar{position:absolute;top:160px;width:300px;text-align:center}
.pillar svg{display:block;margin:0 auto}
.pillar h3{margin-top:18px;font-size:18px;font-weight:700;color:var(--ink);letter-spacing:.5px}
.pillar p{margin-top:14px;font-size:13.5px;line-height:28px;color:var(--white)}

/* contact */
.contact{position:absolute;left:0;top:2322px;width:1200px;height:530px}
.contact .section-title{position:absolute;top:50px;width:100%;text-align:center}
.contact-intro{position:absolute;top:122px;width:100%;text-align:center;font-size:15px;font-weight:500}
.map-bg{position:absolute;left:300px;top:270px;width:640px;height:260px;background:radial-gradient(ellipse at center,rgba(10,110,189,.06),rgba(10,110,189,0) 70%)}
.field{position:absolute;border:1px solid var(--field);background:rgba(255,255,255,.8);font-size:13px;color:var(--muted);padding:16px 12px}
.contact .btn{left:508px;top:420px;width:184px;height:50px;line-height:50px}

/* footer */
.site-footer{position:absolute;left:0;top:2852px;width:1200px;height:148px;background:var(--black)}
.site-footer .brand{left:76px;top:54px}
.footer-links{position:absolute;right:78px;top:54px;text-align:right;color:#d0d0d0;font-size:13.5px;line-height:26px;white-space:nowrap}
.footer-links span{padding:0 6px}
</style>
</head>
<body>

<header class="site-header">
  <div class="brand">HARROW CREEK CAPITAL</div>
  <nav class="main-nav">
    <a class="active" href="#">HOME</a>
    <a href="#">INVESTMENT CRITERIA</a>
    <a href="#">APPROACH</a>
    <a href="#">TEAM</a>
    <a href="#">CONTACT</a>
  </nav>
</header>

<section class="hero">
  <div class="hero-photo" role="img" aria-label="Photo of a wooden cross-rail fence along a green pasture with trees behind"></div>
  <div class="hero-shade"></div>
  <svg class="hero-arrow" style="left:30px" width="24" height="56" viewBox="0 0 24 56"><polyline points="20,4 4,28 20,52" fill="none" stroke="#fff" stroke-width="2"/></svg>
  <svg class="hero-arrow" style="right:30px" width="24" height="56" viewBox="0 0 24 56"><polyline points="4,4 20,28 4,52" fill="none" stroke="#fff" stroke-width="2"/></svg>
  <h1 class="hero-title">HARROW CREEK CAPITAL</h1>
  <p class="hero-tag">Lorem Ipsum is simply dummy text of the printing and type.</p>
  <a class="btn btn-solid" href="#">CONTACT US</a>
</section>

<section class="welcome">
  <h2 class="section-title">WELCOME TO HARROW CREEK</h2>
  <div class="welcome-copy">
    <p>Lorem Ipsum is simply dummy text of the printing and typesetting industry. Lorem Ipsum has been the industry's standard dummy text ever since the 1500s, when an unknown printer took a galley.</p>
    <p>Lorem Ipsum is simply dummy text of the printing and typesetting industry. Lorem Ipsum has been the industry's standard dummy text ever since the 1500s, when an unknown printer took a galley of type and scrambled it to make a type specimen book. It has survived not only five centuries.</p>
  </div>
  <a class="btn btn-outline" href="#">LEARN MORE</a>
</section>

<section class="criteria">
  <h2 class="section-title"><span class="accent">INVESTMENT</span> CRITERIA</h2>
  <svg class="chart" width="860" height="380" viewBox="0 0 860 380" font-family="Raleway, Arial, sans-serif">
    <g stroke="var(--grid)" stroke-width="1">
      <line x1="46" y1="30" x2="842" y2="30"/>
      <line x1="46" y1="80" x2="842" y2="80"/>
      <line x1="46" y1="130" x2="842" y2="130"/>
      <line x1="46" y1="180" x2="842" y2="180"/>
      <line x1="46" y1="230" x2="842" y2="230"/>
      <line x1="46" y1="280" x2="842" y2="280"/>
    </g>
    <g stroke="var(--line)" stroke-width="2">
      <line x1="46" y1="2" x2="46" y2="366"/>
      <line x1="248" y1="2" x2="248" y2="366"/>
      <line x1="460" y1="2" x2="460" y2="366"/>
      <line x1="658" y1="2" x2="658" y2="366"/>
      <line x1="14" y1="330" x2="842" y2="330"/>
    </g>
    <path d="M14 330 C120 300 200 280 270 240 C330 200 400 200 460 188 C540 176 590 168 640 140 C700 104 760 100 832 104" fill="none" stroke="var(--blue)" stroke-width="3"/>
    <text transform="translate(24 170) rotate(-90)" text-anchor="middle" font-size="13" font-weight="700" fill="var(--ink)" letter-spacing="1">LOREM IPSUM TEXT</text>
    <g font-size="13" font-weight="700" fill="var(--ink)" text-anchor="middle">
      <text x="158" y="356">EUROP 15%</text>
      <text x="360" y="356">AFRICA 20%</text>
      <text x="564" y="356">US 30%</text>
      <text x="732" y="356">ASIA 35%</text>
    </g>
  </svg>
  <p class="criteria-copy">Lorem Ipsum is simply dummy text of the printing and typesetting industry. Lorem Ipsum has been the industry's standard dummy text ever since the, when an unknown printer took a galley of type and scrambled it to make a type specimen book.</p>
  <a class="btn btn-solid" href="#">LEARN MORE</a>
</section>

<section class="approach">
  <h2 class="section-title">OUR <span class="dark">APPROACH</span></h2>
  <div class="pillar" style="left:104px">
    <svg width="150" height="150" viewBox="0 0 150 150">
      <circle cx="75" cy="75" r="63" fill="#fff" stroke="#222" stroke-width="4"/>
      <path d="M40 75 Q75 40 110 75 Q75 110 40 75 Z" fill="none" stroke="#222" stroke-width="3"/>
      <circle cx="75" cy="75" r="13" fill="none" stroke="#222" stroke-width="3"/>
      <circle cx="75" cy="75" r="5" fill="#222"/>
    </svg>
    <h3>VISION</h3>
    <p>Lorem Ipsum is simply dummy text of the printing and typesetting industry Ipsum has been the industry's</p>
  </div>
  <div class="pillar" style="left:450px">
    <svg width="150" height="150" viewBox="0 0 150 150">
      <circle cx="75" cy="75" r="68" fill="#222"/>
      <circle cx="75" cy="75" r="61" fill="var(--blue-deep)" stroke="#fff" stroke-width="3"/>
      <g fill="none" stroke="#fff" stroke-width="2.5" stroke-linejoin="round">
        <path d="M55 55 H95 L108 70 L75 108 L42 70 Z"/>
        <path d="M42 70 H108 M62 55 L68 70 L75 108 L82 70 L88 55 M68 70 L75 55 L82 70"/>
      </g>
    </svg>
    <h3>CORE VALUES</h3>
    <p>Lorem Ipsum is simply dummy text of the printing and typesetting industry Ipsum has been the industry's</p>
  </div>
  <div class="pillar" style="left:790px">
    <svg width="150" height="150" viewBox="0 0 150 150">
      <circle cx="75" cy="75" r="63" fill="#fff" stroke="#222" stroke-width="4"/>
      <g fill="none" stroke="#222" stroke-width="3">
        <circle cx="72" cy="78" r="32"/>
        <circle cx="72" cy="78" r="21"/>
        <circle cx="72" cy="78" r="10"/>
        <line x1="72" y1="78" x2="104" y2="46"/>
        <path d="M98 44 L106 36 L108 44 L116 46 L108 54 L102 52"/>
      </g>
    </svg>
    <h3>MISSION</h3>
    <p>Lorem Ipsum is simply dummy text of the printing and typesetting industry Ipsum has been the industry's</p>
  </div>
</section>

<section class="contact">
  <div class="map-bg" role="img" aria-label="Faint dotted world map behind the form"></div>
  <h2 class="section-title"><span class="accent">CONTACT</span> US</h2>
  <p class="contact-intro">If You Need an have any question for Contact Us Today !</p>
  <div class="field" style="left:302px;top:176px;width:292px;height:52px">Name*</div>
  <div class="field" style="left:604px;top:176px;width:292px;height:52px">Phone*</div>
  <div class="field" style="left:302px;top:238px;width:594px;height:52px">Email*</div>
  <div class="field" style="left:302px;top:300px;width:594px;height:104px">Message*</div>
  <a class="btn btn-solid" href="#">SUBMIT</a>
</section>

<footer class="site-footer">
  <div class="brand">HARROW CREEK CAPITAL</div>
  <div class="footer-links">
    <div>Home<span>|</span>Investment Criteria<span>|</span>Approach<span>|</span>Team<span>|</span>Contact</div>
    <div>©ALDERPOINT INVESTMENT GROUP - 2019 All Rights Reserved.</div>
  </div>
</footer>

</body>
</html>
```